Website Design for Morvane.com

We are starting up a business to sell Blutooth devices. Initially speakers and headphones

Morvane of Norway
Leading technology, uncompromised quality.

Specialist in top quality bluetooth equipment
We specialize in design and production of top

```html
<!DOCTYPE html>
<html lang="en">
<head>
<meta charset="utf-8">
<title>Morvane – Quality Bluetooth Speakers</title>
<link href="https://fonts.googleapis.com/css2?family=Roboto:wght@300;400;500;700&family=Roboto+Condensed:wght@400;700&display=swap" rel="stylesheet">
<style>
  :root {
    --page-bg: #ffffff;
    --bar-top: #f4f4f4;
    --bar-bottom: #e6e6e6;
    --border: #dcdcdc;
    --text-dark: #2b2b2b;
    --text-body: #4a4a4a;
    --text-muted: #7a7a7a;
    --brand-green: #7fa51f;
    --button-green: #79a81c;
    --dot: #cfcfcf;
    --dot-active: #666666;
    --speaker-silver: #d6d6d6;
    --speaker-dark: #3a3a3a;
  }
  * { box-sizing: border-box; margin: 0; padding: 0; }
  html, body { width: 1200px; height: 953px; overflow: hidden; background: var(--page-bg); }
  body { position: relative; font-family: "Roboto", Arial, sans-serif; color: var(--text-body); }

  .site-header {
    position: absolute; left: 173px; top: 27px; width: 844px; height: 40px;
    background: linear-gradient(var(--bar-top), var(--bar-bottom));
    border: 1px solid var(--border); border-radius: 3px;
  }
  .brand-name {
    position: absolute; left: 14px; top: 4px;
    font-family: "Roboto", Arial, sans-serif; font-weight: 700; font-size: 27px;
    color: var(--text-dark); letter-spacing: 0.5px;
  }
  .main-nav a {
    position: absolute; top: 11px; font-size: 14px; color: var(--text-muted); text-decoration: none;
  }
  .main-nav a.is-active { color: var(--brand-green); }

  .hero {
    position: absolute; left: 173px; top: 87px; width: 844px; height: 293px;
    border: 1px solid #ececec; border-radius: 4px; background: #fff;
    box-shadow: 0 1px 2px rgba(0,0,0,0.05);
  }
  .hero-title {
    position: absolute; left: 35px; top: 72px;
    font-family: "Roboto Condensed", Arial, sans-serif; font-weight: 700; font-size: 56px;
    color: #3d3d3d; line-height: 1;
  }
  .hero-subtitle {
    position: absolute; left: 37px; top: 129px; font-size: 23px; font-weight: 400; color: #5a5a5a;
  }
  .hero-text {
    position: absolute; left: 37px; top: 160px; width: 440px; font-size: 12px; line-height: 15px; color: var(--text-muted);
  }
  .hero-visual {
    position: absolute; left: 493px; top: 30px; width: 300px; height: 180px; border-radius: 12px;
    background: radial-gradient(ellipse at 45% 60%, var(--speaker-silver), #f5f5f5 65%, #ffffff 80%);
  }
  .slider-dots { position: absolute; left: 730px; top: 268px; display: flex; gap: 8px; }
  .slider-dots span { width: 7px; height: 7px; border-radius: 50%; background: var(--dot); }
  .slider-dots span.is-active { background: var(--dot-active); }

  .product-thumb {
    position: absolute; top: 393px; width: 170px; height: 134px;
    border: 1px solid var(--border); border-radius: 3px; background: #fff; padding: 6px;
  }
  .product-thumb .thumb-image { width: 100%; height: 100%; border-radius: 2px; }
  .thumb-s100 .thumb-image { background: radial-gradient(ellipse at 50% 55%, var(--speaker-silver), #fafafa 75%); }
  .thumb-s200 .thumb-image { background: linear-gradient(90deg, #f4f4f4 0%, #b9b9b9 30%, #9a2020 65%, #f4f4f4 100%); }
  .product-label { position: absolute; top: 530px; width: 170px; text-align: center; font-size: 12px; color: var(--text-dark); }

  .about-heading {
    position: absolute; left: 173px; top: 569px; font-size: 20px; font-weight: 400; line-height: 29px; color: var(--text-dark);
  }
  .about-text {
    position: absolute; left: 175px; top: 625px; width: 440px; font-size: 12.3px; line-height: 15px; color: var(--text-body);
  }
  .quality-heading {
    position: absolute; left: 173px; top: 718px; font-size: 20px; font-weight: 400; color: var(--text-dark);
  }
  .quality-text {
    position: absolute; left: 173px; top: 746px; width: 520px; font-size: 12.3px; line-height: 15px; color: var(--text-body);
  }

  .order-form {
    position: absolute; left: 745px; top: 408px; width: 272px; height: 432px;
    border: 1px solid var(--border); border-radius: 8px; background: #fff;
    box-shadow: 0 2px 3px rgba(0,0,0,0.06);
  }
  .order-title {
    position: absolute; left: 0; top: 14px; width: 100%; text-align: center;
    font-family: "Roboto Condensed", Arial, sans-serif; font-weight: 700; font-size: 31px; color: var(--brand-green);
  }
  .order-field {
    position: absolute; left: 18px; width: 234px; height: 32px;
    border: 1px solid var(--border); border-radius: 16px; background: #fff;
    padding-left: 18px; font-family: "Roboto", Arial, sans-serif; font-size: 12px; color: #888;
    line-height: 30px;
  }
  .send-button {
    position: absolute; left: 158px; top: 384px; width: 94px; height: 33px;
    border: none; border-radius: 17px; background: var(--button-green);
    color: #fff; font-family: "Roboto", Arial, sans-serif; font-weight: 700; font-size: 18px;
  }

  .site-footer {
    position: absolute; left: 173px; top: 885px; width: 844px; height: 38px;
    background: #f0f0f0; border: 1px solid #e2e2e2;
  }
</style>
</head>
<body>
  <header class="site-header">
    <div class="brand-name">Morvane</div>
    <nav class="main-nav">
      <a href="#" class="is-active" style="left:180px">Home</a>
      <a href="#" style="left:271px">About Us</a>
      <a href="#" style="left:374px">Products</a>
      <a href="#" style="left:478px">Contact</a>
    </nav>
  </header>

  <section class="hero">
    <h1 class="hero-title">Morvane S100</h1>
    <h2 class="hero-subtitle">The quality Blutoothspeaker</h2>
    <p class="hero-text">This super-small speaker delivers amazingly high quality sound! The extremely powerful bass system offers a deep and clear sound over the whole spectrum. Charging with Mini USB, 3 hrs music time!</p>
    <div class="hero-visual" role="img" aria-label="Product photo of three S100 bluetooth speakers in silver and black"></div>
    <div class="slider-dots"><span></span><span class="is-active"></span><span></span><span></span><span></span></div>
  </section>

  <div class="product-thumb thumb-s100" style="left:175px">
    <div class="thumb-image" role="img" aria-label="S100 speakers in silver and black"></div>
  </div>
  <div class="product-label" style="left:175px">S100</div>
  <div class="product-thumb thumb-s200" style="left:352px">
    <div class="thumb-image" role="img" aria-label="S200 speakers in silver and red"></div>
  </div>
  <div class="product-label" style="left:352px">S200</div>

  <h2 class="about-heading">Morvane of Norway<br>Leading technology, uncompromised quality.</h2>
  <p class="about-text">Specialist in top quality Bluetooth equipment<br>We specialize in design and production of top quality Bluetooth equipment and we make it available to the world market at a reasonable price based on the shortest possible route from manufacturing to the consumer.</p>

  <h2 class="quality-heading">Quality.</h2>
  <p class="quality-text">Our business concept is based on optimizing design, functionality and quality assurance in making top of the line products available to our customers. Norwegians have for generations represented some of the world's most demanding customers requiring the highest quality of the products consumed. Development and use of leading technologies are also a strong profile of Norwegians documented by the leading role in the use of Information technologies and telecom as well as the leading development of oil exploration and production technologies.</p>

  <form class="order-form">
    <div class="order-title">Order Now!</div>
    <div class="order-field" style="top:57px">First Name</div>
    <div class="order-field" style="top:98px">Middle Name</div>
    <div class="order-field" style="top:139px">Last Name</div>
    <div class="order-field" style="top:180px">Street Name</div>
    <div class="order-field" style="top:221px">House Number</div>
    <div class="order-field" style="top:262px">Post Code</div>
    <div class="order-field" style="top:303px">City/Place</div>
    <div class="order-field" style="top:344px">Country</div>
    <button type="button" class="send-button">Send</button>
  </form>

  <footer class="site-footer"></footer>
</body>
</html>
```